DL size flyer for Autism Consultancy website

We need a printed flyer DL size ( 210mmx99mm) for our Autism Consultancy website www.brightpathkids.nz which provides therapy for autistic children.
I want the flyer to look consistent with the website’s design. Please feel free to use the colour scheme, fonts, icons or any images from www.brightpathkids.nz.It should be easy to see “Autism” or “Autistic” word from a distance.
Please use either an oversized logo or make “Do you have a verbal and able autistic child?” more prominent.
Please do not convert the text fields to outlines, i.e. I need to be able to edit any text after.The final design should be either in Adobe Illustrator or Adobe Photoshop format.
The Specs for the flyer are
Document Trim Size99 x 210 mm 1169 x 2480 pixels
Full Bleed Size102 x 213 mm 1205 x 2516 pixels
Our Logo https://1drv.ms/u/s!AoH0rRjDY2GYg6QtU-xjoVlmslKp6gPlease
use this photo for the front side https://qzdropbin.io/f/Pw4KcN8rTyH2mXs6BvLd9QeFz1Gj
another one for reverse
https://qzdropbin.io/f/Rk2HsV5nWqJ7tZc3MfXb8LpYd4Ne
Please use the following content:
Do you have a verbal and able autistic child?
We use child-centred, modern and innovative approaches
Teaching autistic children to bond, laugh and play.
We work with schools
We help autistic children to develop social minds
We offer:
• Specialist assessments
• Consultations for parents & schools
• Social learning programmes
• Social-cognitive therapy
We can create an individual learning path, best suited for your child.
Our programmes and interventions include:
• Chatter Quest
• Peer Bright
• Team Puzzles
• Tingle Words
• Pebble Tales
• Pembrook Speech Ladder
• Vorlin Method
• BRIMLE Method
• Tandem Pattern Coaching
contact details on both sides:
www.brightpathkids.nz
info@brightpathkids.nz
(09) 57-318-46

```html
<!DOCTYPE html>
<html lang="en">
<head>
<meta charset="utf-8">
<title>DL Flyer – Bright Path Kids Consultancy</title>
<link rel="stylesheet" href="https://fonts.googleapis.com/css2?family=Oswald:wght@400;500;600;700&family=Roboto:wght@400;500&family=Montserrat:wght@400&display=swap">
<style>
:root{
  --stage:#2b2b2b;
  --navy:#1f2d5c;
  --navy-dark:#17234a;
  --teal:#3fcfc0;
  --yellow:#fdd835;
  --orange:#f5a00f;
  --red:#d81e2a;
  --ink:#1f2d5c;
  --paper:#ffffff;
  --black:#151515;
}
*{margin:0;padding:0;box-sizing:border-box}
html,body{width:1160px;height:1200px;overflow:hidden;background:var(--stage)}
body{position:relative;font-family:"Roboto",sans-serif;color:var(--ink)}
.side-label{position:absolute;top:34px;width:449px;text-align:center;color:#fff;font-family:"Montserrat",sans-serif;font-size:34px}
.side-label.front{left:92px}
.side-label.back{left:627px}
.caption{position:absolute;top:1108px;left:0;width:1160px;text-align:center;color:#fff;font-family:"Montserrat",sans-serif;font-size:34px;letter-spacing:.5px}
.flyer{position:absolute;top:106px;width:449px;height:937px;background:var(--paper);overflow:hidden;box-shadow:0 18px 30px rgba(0,0,0,.5)}
.flyer.front{left:92px}
.flyer.back{left:627px}
.abs{position:absolute}

/* front */
.brand{left:0;top:30px;width:449px;display:flex;align-items:center;justify-content:center;gap:12px}
.brand-dot{width:44px;height:44px;border-radius:50%;background:var(--yellow)}
.brand-name{font-family:"Oswald",sans-serif;font-weight:600;font-size:26px;line-height:1.05;color:var(--navy)}
.headline{left:0;top:128px;width:449px;text-align:center;font-family:"Oswald",sans-serif;font-weight:500;font-size:25px;line-height:30px;color:var(--navy)}
.headline .hl{color:var(--teal)}
.front-photo{left:0;top:196px;width:449px;height:440px;background:linear-gradient(160deg,#e9eef2 0%,#d9c9b0 45%,#b77a52 75%,#8aa0b8 100%)}
.navy-base{left:0;top:600px;width:449px;height:337px;background:linear-gradient(180deg,var(--navy) 0%,var(--navy-dark) 100%)}
.question-block{left:44px;top:530px;width:365px;height:185px;background:var(--black);transform:rotate(-1deg)}
.q-small{left:0;top:542px;width:449px;text-align:center;color:#fff;font-family:"Oswald",sans-serif;font-weight:500;font-size:21px}
.q-big{left:0;top:565px;width:449px;text-align:center;color:var(--yellow);font-family:"Oswald",sans-serif;font-weight:700;font-size:100px;line-height:100px;letter-spacing:-2px}
.q-child{left:0;top:660px;width:449px;text-align:center;color:var(--teal);font-family:"Oswald",sans-serif;font-weight:600;font-size:46px;line-height:50px}
.path-text{left:34px;top:724px;width:300px;text-align:center;color:#fff;font-family:"Oswald",sans-serif;font-weight:500;font-size:17px;line-height:24px}
.stamp{left:330px;top:672px;width:92px;height:92px;border-radius:50%;border:5px solid var(--red);display:flex;align-items:center;justify-content:center;transform:rotate(-18deg)}
.stamp span{color:var(--red);font-family:"Oswald",sans-serif;font-weight:700;font-size:13px;line-height:14px;text-align:center}
.contact-btn{left:130px;top:790px;width:190px;height:48px;border-radius:24px;border:2px solid #fff;background:linear-gradient(180deg,var(--yellow) 0%,var(--orange) 100%);display:flex;align-items:center;justify-content:center;font-family:"Oswald",sans-serif;font-weight:600;font-size:28px;color:var(--black)}
.phone{left:0;top:850px;width:449px;display:flex;align-items:center;justify-content:center;gap:10px;color:#fff;font-family:"Oswald",sans-serif;font-weight:500;font-size:32px}
.contact-line{left:0;top:902px;width:449px;display:flex;justify-content:center;gap:14px;color:#fff;font-size:14px}
.contact-line span{display:flex;align-items:center;gap:6px}
.ico{width:18px;height:18px;flex:none}

/* back */
.pill{background:var(--teal);color:#fff;border-radius:20px;font-family:"Oswald",sans-serif;font-weight:500;display:flex;align-items:center;justify-content:center}
.how-pill{left:145px;top:32px;width:160px;height:32px;font-size:21px}
.intro{left:0;top:76px;width:449px;text-align:center;font-size:14px;line-height:20px}
.intro strong{font-weight:500}
.offer-list{left:30px;top:124px;width:400px;display:grid;grid-template-columns:185px 215px;row-gap:4px;list-style:none;font-size:14px;line-height:19px}
.offer-list li{position:relative;padding-left:16px}
.offer-list li::before{content:"";position:absolute;left:0;top:6px;width:7px;height:7px;border-radius:50%;background:var(--yellow)}
.tag-band{left:0;top:198px;width:449px;height:36px;background:var(--navy);color:var(--yellow);font-family:"Oswald",sans-serif;font-weight:500;font-size:20px;display:flex;align-items:center;justify-content:center}
.steps{left:0;top:250px;width:449px;display:flex;justify-content:center;gap:22px;font-family:"Oswald",sans-serif;font-weight:500;font-size:23px;color:var(--navy)}
.steps span{display:flex;align-items:center;gap:7px}
.steps b{width:30px;height:30px;border-radius:50%;background:var(--yellow);color:#fff;font-weight:500;font-size:20px;display:flex;align-items:center;justify-content:center}
.prog-pill{left:73px;top:302px;width:303px;height:34px;font-size:19px}
.programs{left:16px;top:350px;width:418px;display:grid;grid-template-columns:repeat(4,1fr);row-gap:8px;text-align:center;font-size:15px;line-height:20px;color:var(--navy)}
.programs div{display:flex;flex-direction:column;align-items:center;gap:4px}
.programs svg{width:26px;height:26px}
.programs .last{grid-column:2 / span 2}
.testimonial{left:0;top:604px;width:449px;height:156px;background:var(--yellow)}
.quote-mark{left:24px;top:606px;color:#fff;opacity:.6;font-family:"Oswald",sans-serif;font-weight:700;font-size:70px;line-height:70px}
.test-title{left:86px;top:618px;color:#fff;font-family:"Oswald",sans-serif;font-weight:600;font-size:24px}
.test-text{left:26px;top:658px;width:212px;font-size:11.5px;line-height:17px;color:var(--navy)}
.back-navy{top:750px;height:187px}
.circle-photo{left:250px;top:558px;width:230px;height:230px;border-radius:50%;border:6px solid #f1f1f1;background:radial-gradient(circle at 45% 50%,#e8c9a6 0%,#d6a978 40%,#c49a6a 70%,#9b7b58 100%)}
</style>
</head>
<body>
<div class="side-label front">Front</div>
<div class="side-label back">Back</div>

<section class="flyer front">
  <div class="abs brand"><div class="brand-dot"></div><div class="brand-name">Bright Path Kids<br>Consultancy</div></div>
  <h1 class="abs headline">We use child-centred, <span class="hl">Modern &amp;</span><br><span class="hl">Innovative</span> approaches</h1>
  <div class="abs front-photo" role="img" aria-label="Photo: therapist playing with a smiling boy holding a teddy bear in a bright playroom"></div>
  <svg class="abs" style="left:0;top:560px" width="449" height="80" viewBox="0 0 449 80" aria-hidden="true">
    <path d="M0 40 Q30 10 60 40 T120 40 T180 40 T240 40 T300 40 T360 40 T420 40 T480 40 V80 H0Z" fill="var(--yellow)"/>
  </svg>
  <div class="abs navy-base"></div>
  <div class="abs question-block"></div>
  <p class="abs q-small">Do you have a verbal and able</p>
  <p class="abs q-big">Autistic</p>
  <p class="abs q-child">Child?</p>
  <p class="abs path-text">We can create an individual learning<br>path, best suited for your child.</p>
  <div class="abs stamp"><span>WE<br>WORK WITH<br>SCHOOLS</span></div>
  <div class="abs contact-btn">Contact Us</div>
  <div class="abs phone">
    <svg width="24" height="24" viewBox="0 0 24 24" aria-hidden="true"><circle cx="12" cy="12" r="12" fill="var(--yellow)"/><path d="M8 6l2.5 0.5 1 3-1.5 1a6 6 0 0 0 3.5 3.5l1-1.5 3 1 .5 2.5c-5 1-11-5-10-10z" fill="var(--navy)"/></svg>
    (09) 57-318-46
  </div>
  <div class="abs contact-line">
    <span><svg class="ico" viewBox="0 0 18 18" aria-hidden="true"><circle cx="9" cy="9" r="9" fill="var(--yellow)"/><rect x="4.5" y="6" width="9" height="6.5" fill="var(--navy)"/><path d="M4.5 6l4.5 3.5 4.5-3.5" stroke="var(--yellow)" fill="none"/></svg>info@brightpathkids.nz</span>
    <span><svg class="ico" viewBox="0 0 18 18" aria-hidden="true"><circle cx="9" cy="9" r="9" fill="var(--yellow)"/><circle cx="9" cy="9" r="5" stroke="var(--navy)" stroke-width="1.3" fill="none"/><path d="M4 9h10M9 4v10" stroke="var(--navy)" stroke-width="1.2"/></svg>www.brightpathkids.nz</span>
  </div>
</section>

<section class="flyer back">
  <div class="abs pill how-pill">HOW WE HELP</div>
  <p class="abs intro">We help autistic children to develop social minds<br><strong>WE OFFER:</strong></p>
  <ul class="abs offer-list">
    <li>Specialist assessments</li>
    <li>Social learning programmes</li>
    <li>Consultations for parents &amp; schools</li>
    <li>Social-cognitive therapy</li>
  </ul>
  <div class="abs tag-band">Teaching autistic children to bond, laugh and play.</div>
  <div class="abs steps"><span><b>1</b>Analyse</span><span><b>2</b>Consult</span><span><b>3</b>Develop</span></div>
  <div class="abs pill prog-pill">Programs &amp; Therapeutic Interventions</div>
  <div class="abs programs">
    <div><svg viewBox="0 0 26 26"><path d="M3 6h9v15H3zM14 6h9v15h-9z" fill="none" stroke="var(--yellow)" stroke-width="2"/></svg>Pebble<br>Tales</div>
    <div><svg viewBox="0 0 26 26"><ellipse cx="12" cy="11" rx="9" ry="6" fill="none" stroke="var(--yellow)" stroke-width="2"/><path d="M8 16l-2 5 6-4" fill="none" stroke="var(--yellow)" stroke-width="2"/></svg>Pembrook<br>Speech Ladder</div>
    <div><svg viewBox="0 0 26 26"><path d="M8 5l8 8-8 8M18 5l-4 4" fill="none" stroke="var(--yellow)" stroke-width="2.5"/></svg>Vorlin<br>Method</div>
    <div><svg viewBox="0 0 26 26"><circle cx="13" cy="11" r="6" fill="none" stroke="var(--yellow)" stroke-width="2"/><path d="M10 19h6M11 22h4" stroke="var(--yellow)" stroke-width="2"/></svg>Chatter<br>Quest</div>
    <div><svg viewBox="0 0 26 26"><circle cx="13" cy="13" r="5" fill="none" stroke="var(--yellow)" stroke-width="2"/><path d="M13 2v4M13 20v4M2 13h4M20 13h4" stroke="var(--yellow)" stroke-width="2"/></svg>Peer<br>Bright</div>
    <div><svg viewBox="0 0 26 26"><circle cx="8" cy="8" r="4" fill="none" stroke="var(--yellow)" stroke-width="2"/><circle cx="18" cy="8" r="4" fill="none" stroke="var(--yellow)" stroke-width="2"/><circle cx="8" cy="18" r="4" fill="none" stroke="var(--yellow)" stroke-width="2"/><circle cx="18" cy="18" r="4" fill="none" stroke="var(--yellow)" stroke-width="2"/></svg>Team<br>Puzzles</div>
    <div><svg viewBox="0 0 26 26"><circle cx="13" cy="12" r="9" fill="none" stroke="var(--yellow)" stroke-width="2"/><path d="M13 16l-4-4a2.5 2.5 0 0 1 4-3 2.5 2.5 0 0 1 4 3z" fill="none" stroke="var(--yellow)" stroke-width="1.6"/></svg>Tingle<br>Words</div>
    <div><svg viewBox="0 0 26 26"><path d="M6 22L20 4M12 12c4-6 10-8 10-8s-2 8-8 10" fill="none" stroke="var(--yellow)" stroke-width="2.2"/></svg>BRIMLE<br>Method</div>
    <div class="last"><svg viewBox="0 0 26 26"><path d="M8 4v18M8 14a5 5 0 1 1 0 8M12 8l8 3" fill="none" stroke="var(--yellow)" stroke-width="2.2"/></svg>Tandem<br>Pattern Coaching</div>
  </div>
  <div class="abs testimonial"></div>
  <svg class="abs" style="left:0;top:588px" width="449" height="30" viewBox="0 0 449 30" aria-hidden="true">
    <path d="M0 30 V18 Q20 0 40 18 T80 18 T120 18 T160 18 T200 18 T240 18 T280 18 T320 18 T360 18 V30Z" fill="var(--yellow)"/>
  </svg>
  <div class="abs quote-mark">“</div>
  <h2 class="abs test-title">TESTIMONIALS</h2>
  <p class="abs test-text">Miriam is extremely passionate about helping people with autism, my son thoroughly enjoyed his sessions which helped to boost his confidence and social skills.</p>
  <div class="abs navy-base back-navy"></div>
  <svg class="abs" style="left:0;top:740px" width="449" height="24" viewBox="0 0 449 24" aria-hidden="true">
    <path d="M0 0 H449 V12 Q429 24 409 12 T369 12 T329 12 T289 12 T249 12 T209 12 T169 12 T129 12 T89 12 T49 12 T9 12 T-31 12Z" fill="var(--yellow)"/>
  </svg>
  <div class="abs circle-photo" role="img" aria-label="Photo: young boy in a striped shirt playing with toy cars on a wooden floor"></div>
  <div class="abs contact-btn">Contact Us</div>
  <div class="abs phone">
    <svg width="24" height="24" viewBox="0 0 24 24" aria-hidden="true"><circle cx="12" cy="12" r="12" fill="var(--yellow)"/><path d="M8 6l2.5 0.5 1 3-1.5 1a6 6 0 0 0 3.5 3.5l1-1.5 3 1 .5 2.5c-5 1-11-5-10-10z" fill="var(--navy)"/></svg>
    (09) 57-318-46
  </div>
  <div class="abs contact-line">
    <span><svg class="ico" viewBox="0 0 18 18" aria-hidden="true"><circle cx="9" cy="9" r="9" fill="var(--yellow)"/><rect x="4.5" y="6" width="9" height="6.5" fill="var(--navy)"/><path d="M4.5 6l4.5 3.5 4.5-3.5" stroke="var(--yellow)" fill="none"/></svg>info@brightpathkids.nz</span>
    <span><svg class="ico" viewBox="0 0 18 18" aria-hidden="true"><circle cx="9" cy="9" r="9" fill="var(--yellow)"/><circle cx="9" cy="9" r="5" stroke="var(--navy)" stroke-width="1.3" fill="none"/><path d="M4 9h10M9 4v10" stroke="var(--navy)" stroke-width="1.2"/></svg>www.brightpathkids.nz</span>
  </div>
</section>

<p class="caption">DL SIZE FLYER FOR AUTISM CONSULTANCY WEBSITE</p>
</body>
</html>
```